Looking for a modern website banner design

Bramblecrest Coaching Partners looking for the development of the main banner of the website. The project description and photos are included in the upload files.

```html
<!DOCTYPE html>
<html lang="en">
<head>
<meta charset="utf-8">
<title>Bramblecrest Coaching Partners – Testimonial Banner</title>
<link rel="stylesheet" href="https://fonts.googleapis.com/css2?family=Lato:wght@400;700;900&family=Fjalla+One&display=swap">
<style>
  :root {
    --navy: #2b2e62;
    --navy-deep: #22244f;
    --white: #ffffff;
    --button-blue: #1f6bb3;
    --crowd-dark: #2a2430;
    --crowd-warm: #4a3238;
    --ice: #eef0f5;
  }
  * { margin: 0; padding: 0; box-sizing: border-box; }
  html, body { width: 1200px; height: 675px; overflow: hidden; }
  body { font-family: "Lato", sans-serif; background: var(--navy); }

  .banner {
    position: relative;
    width: 1200px;
    height: 675px;
    overflow: hidden;
    background: radial-gradient(circle at 20% 30%, #34387a 0%, var(--navy) 55%, var(--navy-deep) 100%);
  }

  .action-photo {
    position: absolute;
    top: 0; right: 0;
    width: 760px;
    height: 675px;
    background:
      linear-gradient(90deg, var(--navy) 0%, rgba(43,46,98,0.85) 18%, rgba(43,46,98,0.2) 45%, rgba(43,46,98,0) 60%),
      linear-gradient(180deg, var(--crowd-dark) 0%, var(--crowd-warm) 45%, #6b4a4e 52%, #d9d8e0 72%, var(--ice) 100%);
  }

  .testimonial {
    position: absolute;
    left: 34px;
    top: 197px;
    width: 518px;
    height: 269px;
    border: 2px solid var(--white);
    border-bottom: none;
  }
  .testimonial__base {
    position: absolute;
    bottom: 0;
    height: 2px;
    background: var(--white);
  }
  .testimonial__base--left { left: -2px; width: 12px; }
  .testimonial__base--right { left: 152px; right: -2px; }
  .testimonial__dot {
    position: absolute;
    bottom: -4px;
    width: 9px; height: 9px;
    border-radius: 50%;
    background: var(--white);
  }
  .testimonial__dot--left { left: 6px; }
  .testimonial__dot--right { left: 147px; }

  .quote-mark { position: absolute; display: block; }
  .quote-mark--open { left: 16px; top: 16px; }
  .quote-mark--close { display: inline-block; vertical-align: -6px; margin-left: 12px; }

  .testimonial__headline {
    position: absolute;
    left: 18px;
    top: 12px;
    width: 490px;
    color: var(--white);
    font-weight: 700;
    font-size: 22.5px;
    line-height: 36px;
    text-indent: 40px;
  }
  .testimonial__body {
    position: absolute;
    left: 18px;
    top: 122px;
    width: 495px;
    color: var(--white);
    font-size: 18.5px;
    line-height: 25px;
  }
  .testimonial__body strong { font-weight: 700; }

  .testimonial__attribution {
    position: absolute;
    left: 18px;
    top: 211px;
    color: var(--white);
    font-family: "Fjalla One", sans-serif;
    font-size: 18.5px;
    letter-spacing: 0.2px;
    white-space: nowrap;
  }
  .testimonial__attribution .divider { margin: 0 12px; }

  .cta-button {
    position: absolute;
    left: 54px;
    top: 448px;
    width: 125px;
    height: 30px;
    background: var(--button-blue);
    color: var(--white);
    font-size: 8px;
    font-weight: 900;
    letter-spacing: 0.4px;
    text-transform: uppercase;
    text-decoration: none;
    display: flex;
    align-items: center;
    justify-content: center;
  }
</style>
</head>
<body>
  <main class="banner">
    <div class="action-photo" role="img" aria-label="Hockey player celebrating a goal on the ice in front of a cheering crowd, with an opposing player skating in the foreground"></div>

    <section class="testimonial">
      <svg class="quote-mark quote-mark--open" width="34" height="32" viewBox="0 0 34 32" aria-hidden="true">
        <path d="M0 0h14v12c0 9-4 16-10 20l-2-3c3-3 4-6 4-10H0z" fill="#fff"/>
        <path d="M18 0h14v12c0 9-4 16-10 20l-2-3c3-3 4-6 4-10h-6z" fill="#fff"/>
      </svg>
      <p class="testimonial__headline">Bramblecrest has provided support that has allowed me to develop as a person and an athlete.</p>
      <p class="testimonial__body"><strong>The S.T.R.I.D.E.™</strong> process allowed me to stay focused on attainable goals each season and progress from Junior to College and now Professional Hockey.<svg class="quote-mark quote-mark--close" width="34" height="32" viewBox="0 0 34 32" aria-hidden="true">
        <path d="M14 32H0V20C0 11 4 4 10 0l2 3C9 6 8 9 8 13h6z" fill="#fff"/>
        <path d="M32 32H18V20c0-9 4-16 10-20l2 3c-3 3-4 6-4 10h6z" fill="#fff"/>
      </svg></p>
      <p class="testimonial__attribution">Marcus Delaine<span class="divider">|</span>Riverton Falcons<span class="divider">|</span>Atlantic Pro Hockey Circuit</p>

      <span class="testimonial__base testimonial__base--left"></span>
      <span class="testimonial__base testimonial__base--right"></span>
      <span class="testimonial__dot testimonial__dot--left"></span>
      <span class="testimonial__dot testimonial__dot--right"></span>
    </section>

    <a class="cta-button" href="#">Try Bramblecrest</a>
  </main>
</body>
</html>
```